Contemporary Media Company with Logo Needs Business Card Design

Need a modern card design for a full service digital media company using the logo included. Also want the info below on the card. Probably list the services on the card back to save space for the front. Want something contemporary to impress prospective clients. You may want to submit both a somewhat more conservative design, and then a more wild one.
General Info: (this phrase need not be on the card)
Ned Parlow
Founder and CEO
949-612-4830
ned@vontaramedia.example
vontaramedia.example
Services: (this word need not be on the card)
Content & Experience Strategy
Brand Development
Search Engine Optimization
Website Design
Website Operation
Social Media Integration
Complete Video Solutions
Updates
Industry/Entity Type
Business
Contact Information for Business Card
Ned Parlow
Founder and CEO
949-612-4830
ned@vontaramedia.example
vontaramedia.example
Brand Development
Website Design
Website Operation
Social Media Integration
Complete Video Solutions
Look and feel
Each slider illustrates characteristics of the customer's brand and the style your logo design should communicate.

```html
<!DOCTYPE html>
<html lang="en">
<head>
<meta charset="utf-8">
<title>Vontara Media – Business Cards</title>
<link rel="stylesheet" href="https://fonts.googleapis.com/css2?family=Open+Sans:wght@400;600&display=swap">
<style>
  :root {
    --orange: #ee7623;
    --grey: #6d6e71;
    --ink: #2b2b2b;
    --card: #ffffff;
    --stage: #e6e6e6;
  }
  * { box-sizing: border-box; margin: 0; padding: 0; }
  html, body { width: 1200px; height: 750px; overflow: hidden; }
  body {
    background: var(--stage);
    font-family: "Open Sans", Arial, sans-serif;
    color: var(--ink);
    display: flex;
    align-items: center;
    justify-content: center;
    gap: 60px;
  }
  .card {
    width: 520px;
    height: 297px;
    background: var(--card);
    box-shadow: 0 6px 18px rgba(0,0,0,0.18);
    position: relative;
  }

  /* Back: name and services */
  .card-back {
    display: flex;
    flex-direction: column;
    align-items: center;
    justify-content: center;
    padding: 0 40px;
  }
  .brand-block {
    display: flex;
    align-items: center;
    gap: 12px;
    margin-bottom: 30px;
  }
  .brand-square {
    width: 30px; height: 30px;
    background: var(--orange);
  }
  .brand-name {
    font-size: 30px;
    font-weight: 600;
    color: var(--orange);
    letter-spacing: 0.04em;
  }
  .services {
    width: 100%;
    border-top: 1.5px solid var(--orange);
    border-bottom: 1.5px solid var(--orange);
    padding: 12px 0;
    text-align: center;
    font-size: 13px;
    line-height: 1.5;
    color: var(--ink);
  }
  .services .dot {
    display: inline-block;
    width: 5px; height: 5px;
    background: var(--orange);
    margin: 0 6px;
    vertical-align: middle;
  }

  /* Front: contact */
  .card-front { padding: 36px 40px; }
  .front-brand {
    display: flex;
    align-items: center;
    gap: 10px;
  }
  .front-brand .brand-square { width: 22px; height: 22px; background: var(--grey); }
  .front-brand .brand-name {
    font-size: 26px;
    font-weight: 400;
    color: var(--grey);
    letter-spacing: 0.06em;
  }
  .person { margin: 34px 0 0 150px; }
  .person-name {
    font-size: 20px;
    font-weight: 400;
    color: var(--orange);
  }
  .person-title { font-size: 14px; color: var(--ink); }
  .contact-list {
    list-style: none;
    margin: 26px 0 0 150px;
    font-size: 15px;
    line-height: 1.45;
  }
  .contact-list li { display: flex; align-items: center; gap: 8px; }
  .contact-list svg { width: 14px; height: 14px; fill: var(--orange); flex: none; }
</style>
</head>
<body>

  <section class="card card-back">
    <div class="brand-block">
      <span class="brand-square"></span>
      <span class="brand-name">VONTARA MEDIA</span>
    </div>
    <div class="services">
      Content &amp; Experience Strategy<span class="dot"></span>Brand Development<br>
      Search Engine Optimization<span class="dot"></span>Website Design<span class="dot"></span>Website Operation<br>
      Social Media Integration<span class="dot"></span>Complete Video Solutions
    </div>
  </section>

  <section class="card card-front">
    <div class="front-brand">
      <span class="brand-square"></span>
      <span class="brand-name">VONTARA MEDIA</span>
    </div>
    <div class="person">
      <p class="person-name">Ned Parlow</p>
      <p class="person-title">Founder and CEO</p>
    </div>
    <ul class="contact-list">
      <li>
        <svg viewBox="0 0 16 16" aria-hidden="true"><path d="M3 1h3l1.5 4-2 1.3a9 9 0 0 0 4.2 4.2L11 8.5l4 1.5v3a2 2 0 0 1-2 2A12 12 0 0 1 1 3a2 2 0 0 1 2-2z"/></svg>
        949-612-4830
      </li>
      <li>
        <svg viewBox="0 0 16 16" aria-hidden="true"><path d="M1 3h14v10H1z M2 4l6 5 6-5" fill="none" stroke="#ee7623" stroke-width="1.6"/></svg>
        ned@vontaramedia.example
      </li>
      <li>
        <svg viewBox="0 0 16 16" aria-hidden="true"><path d="M8 0a5.5 5.5 0 0 0-5.5 5.5C2.5 10 8 16 8 16s5.5-6 5.5-10.5A5.5 5.5 0 0 0 8 0zm0 8a2.5 2.5 0 1 1 0-5 2.5 2.5 0 0 1 0 5z"/></svg>
        vontaramedia.example
      </li>
    </ul>
  </section>

</body>
</html>
```